Quiz Dale Penrose (Page Forge or Flinket template)

Business Name?
Quiz Dale Penrose (QuizDalePenrose.com) Technically, this is the name of the web site. This is a venture, rather than a business. It is part of building my brand as an expert.

- What do you do?
I am a life strategist/coach (http://VelotrimGroup.example/). This site will be a one-stop advice site, providing answers to real life challenges. The tagline is "life challenges, real solutions." It is a three step process: ASK-RECEIVE-ACHIEVE. It should, however, be FUN/ENGAGING (yet useful), rather than have a business/consultant feel. Approachable!

- How many pages do you need designed and code?
The site will have 7 sections:
Home (this is where I envision the introductory text, the ability for the user to submit their questions and they will be visible for all to see)
About Dale (my bio information/fascinating facts)
Dale's Notes (my blog-discussing general personal development topics and comments from readers)
Audio/Video (video tips and an audio player from chatwaveaudio.example that enables visitors to listen to my radio show/podcast)
Donations (this is where visitors can donate after they have had their questions answered. I am not attached to a specific vendor as long as it is NOT CoinRelay-perhaps Zentra Pay. I need to have designated dollar increments that people can select-perhaps in $5 or $10 intervals)
Contact Dale (contact information and perhaps a VOXLY access button so that they can immediately contact me; it might be nice to have a chat room here for online chat, but I don't see this as vital)

- What is your industry?
Consulting/Professional Services

- Describe the target audience for your website design?
EVERYONE! I am going to becoming the "go-to guy" for when you are feeling stuck.

- What 3 things would you like to communicate to your audience through your website design?
Insightful, Engaging, Wise (& FUN, FUN, FUN!). This is not a traditional business site. I have one of those. It should be fun & cutting-edge.

- How is your company different from your competitors?
It is not what I do that is different. It is my approach. I believe that success is a product of conditioning. Rather than simply focusing on what you are doing (which is, naturally, important), you must also focus on who you are. "YOU" are the common denominator in all that you do!

- What website design styles do you like?
I tend to be attracted to fashion/photography/artist web sites. I love this Flinket Lidbox design:
http://skinbazaar.example/item/lidbox/full_screen_preview/7739205
I would love to have this style of menu navigation (these type of icons).

- What colors do you want to see in your website design?
I am completely open at this point (I have a couple of people working on a logo. It's not done yet. I now that it incorporates black & red, so, a black background might be nice). Naturally, this could influence it. I like "slick, sleek and cutting edge-something that will pop off the screen!

- What colors do you NOT want to see in your website design?
No restrictions as long as they are utilized in the appropriate balance/combination.

- What adjectives should best describe your website design?
Slick, sleek, cutting edge, cool, engaging, artistic

- What content must be included in the website design?
In addition to my logo and tagline : "life challenges, real solutions," I want to feature: ASK-RECEIVE-ACHIEVE somewhere.

- Do you have additional requirements or links you want to share?
The primary challenge (and unlike most web sites) is that the main section is user-driven. The user submits the questions and I respond after it is posted (unlike a typical blog where I post and users comment). In an ideal world I would like for the user to be able to select from one of six categories while submitting their question.(Relationships, Health/Body, Career/Work Life, Spirituality, Money/Finance, Other). Then, when the user selects their category, their question would be displayed in the appropriate section. The challenge with that is that I need to have at least some q&a displayed on the home page so that visitors get an immediate sense of what I am doing. I want to have the ability to also response to submitted questions via video should I choose to do so. I want visitors to be able to share postings/my responses on Chatterly, Peepline, etc.

Page Forge has 3 templates that enable this q&a capability, but they are very unattractive in their design (like tech help forums-EW!) and they seem to require users to create their own profile page, etc. I don't see that as necessary. I don't know what can be modified, turned off, etc.
http://toppfhelpdesk.example/the-best-pageforge-themes-for-creating-qa-websites/
Updates

First of all: Thank you for bringing your creative gifts/talents/expertise to my challenge!

I assume it is sometimes challenging having to fill space without the actual words, so I have attached some documents that I am hoping will be helpful.

Logo-I didn't know what type of file you need, so I have attached .jpg, .pns, .eps
Pictures-I will be having some professional pics taken, but in the interim, I have attached 3 that can be used. I like the one with the hat as the main pic.
Documents:
-Quiz Dale Penrose Home-this is the text for the introduction that precedes the Q&A section on the home page
-About Dale/25 Random Facts-for the About Dale section.
-Dale's Notes-I have attached some blog entries for this section

If you have any questions, please do not hesitate to contact me. Thanks, again, for joining me. Please know that I work without a great many people who are in need of good designers for their projects/businesses. I will happily direct them to the people with the best talents when we are through. I want this to be a win-win for all of us!

Hello Designers!

I wanted to take a moment to stress that I really want something "cutting-edge." I am NOT looking for something that is traditional (and especially not something that has a corporate/consultant flavor). I want FUN. As I have stated-think artist/fashion/creative. I referred you all to the Flinket design because I like that look at feel. I like the navigation icons and the navigation of that template. Because I like cutting edge, please refrain from the use of stock photography or clip art.

I really need for users to know immediately what this site is all about-right from the home page, without having to navigate around. I have always envisioned q&a being on the home page. If this cannot work, I am open to alternatives, as long as it is clear what the site is about. 

I attached the logo, the intro text and some text for other sections for a reason. Please use it! This will enable me to truly envision what you see and how this should all blend together. Thank you so much.

If I can provide any additional information or assistance, please do not hesitate to contact me. 

Hello Designers:

I had a slight modification made to the logo (a little more white space-think you'll like it better). I deleted the old files and uploaded new attachments of the revised logo. I wasn't sure which file format you prefer to work with so I included a few!

Please do not hesitate to ask any questions should they arise. Thanks for your hard work.

Dale

Reason: Since many seem to be pressed to participate due to competing schedules, I am adding a couple more days. Only a couple! Before submitting a design, please pay close attention to my brief. I must see how the home page intro and the q&a will be incorporated and displayed. To all who choose to contribute their gifts and talents to this challenge, I really appreciate it. Thanks! Dale

Target Market(s)

EVERYONE! Yes, the world!

Industry/Entity Type

Building

Requirements
Must have
• There can be no compromise in the user-driven question and answer capability (where the questions are clearly displayed for all to see). This is the point of the entire site, so without it, there is no point!

All have my desired sections have already been detailed above.
Should not have
• I do not want this site to look like a typical coaching or corporate consulting site. Fun, engaging, cutting edge & forward thinking!

```html
<!DOCTYPE html>
<html lang="en">
<head>
<meta charset="utf-8">
<title>Quiz Dale Penrose – life challenges · real solutions</title>
<link rel="stylesheet" href="https://fonts.googleapis.com/css2?family=Oswald:wght@300;700&family=Arimo:ital,wght@0,400;0,700;1,400&display=swap">
<style>
:root{
  --red:#d3121b;
  --ink:#2b2b2b;
  --grey:#9a9a9a;
  --frame:#a9a9ad;
  --card:#ffffff;
  --panel:#ececee;
  --ribbon:#d4d4d6;
  --salmon:#e4705e;
  --skin:#f0b98a;
}
*{box-sizing:border-box;margin:0;padding:0}
html,body{width:960px;height:1200px;overflow:hidden}
body{position:relative;background:linear-gradient(#fbfbfc,#e9e9ec 45%,#f3f3f5);font-family:Arimo,Helvetica,sans-serif;color:var(--ink)}
.abs{position:absolute}

.brand{left:0;width:960px;top:40px;text-align:center;font-family:Oswald,sans-serif;font-weight:700;font-size:46px;line-height:56px;color:var(--red);letter-spacing:-1px;text-transform:uppercase}
.tagline{left:0;width:960px;top:114px;text-align:center;font-size:16px;color:var(--ink)}

.main-nav{left:96px;top:158px;width:776px;font-family:Oswald,sans-serif;font-weight:300;font-size:32px;line-height:44px;letter-spacing:-.6px;color:#3a3a3a;white-space:nowrap;text-transform:uppercase}
.main-nav span{margin:0 5px}

.step-art{border-radius:50%;background:radial-gradient(ellipse at 50% 45%,var(--skin) 0 55%,#d98a52 75%,transparent 77%)}
.step-arrow{top:296px}
.step-word{font-family:Oswald,sans-serif;font-weight:700;color:var(--red);text-transform:uppercase;font-size:48px;line-height:56px;letter-spacing:-1px;text-align:center}

.icon-bar{left:260px;top:487px;height:28px;display:flex;gap:6px}
.icon-bar .dot{width:28px;height:28px;border-radius:50%;background:#1c1c1c;box-shadow:0 1px 2px rgba(0,0,0,.5);display:flex;align-items:center;justify-content:center}
.icon-bar .gap{width:8px}

.qa-card{width:230px;height:312px;top:530px;border:2px solid var(--frame);border-radius:24px;background:var(--panel)}
.qa-inner{position:absolute;left:13px;top:13px;width:200px;height:289px;background:var(--card);border-radius:14px;padding:10px 0 0 4px}
.qa-title{font-weight:700;font-size:13px;color:var(--red);text-transform:uppercase}
.qa-cat{font-style:italic;font-size:12.5px;color:#b5b5b5;margin:4px 0 3px -2px;letter-spacing:-.4px}
.qa-body{font-size:12.3px;line-height:16.3px;letter-spacing:-.45px;color:#111;white-space:nowrap}
.more-btn{position:absolute;right:-2px;bottom:-6px;width:84px;height:26px;border-radius:3px;background:linear-gradient(#ef8a79,var(--salmon));box-shadow:1px 2px 3px rgba(0,0,0,.35);color:#fff;font-size:13px;display:flex;align-items:center;justify-content:center;gap:6px;letter-spacing:-.4px}

.video-panel{left:106px;top:886px;width:490px;height:312px;border:2px solid var(--frame);border-radius:24px;background:var(--panel)}
.video-inner{position:absolute;left:12px;top:12px;width:462px;height:300px;background:var(--card);border-radius:16px}
.video-heading{left:314px;top:862px;width:86px;text-align:center;font-family:Oswald,sans-serif;font-weight:700;font-size:32px;line-height:40px;color:var(--red)}
.video-frame{left:150px;top:924px;width:400px;height:244px;background:linear-gradient(135deg,#4a3a2c,#8a7456 55%,#cfc3a8)}
.video-title{position:absolute;left:9px;top:6px;color:#fff;font-weight:700;font-size:13px;letter-spacing:-.3px;text-shadow:0 1px 2px #000}
.video-play{position:absolute;left:172px;top:94px;width:54px;height:38px;border-radius:7px;background:rgba(210,210,210,.85);display:flex;align-items:center;justify-content:center}
.video-mark{position:absolute;right:8px;bottom:26px;color:rgba(255,255,255,.8);font-size:13px;font-weight:700}
.video-controls{position:absolute;left:0;bottom:0;width:400px;height:20px;background:linear-gradient(#f4f4f4,#cfcfcf);font-size:8px;display:flex;align-items:center;gap:8px;padding-left:8px}
.video-controls .track{flex:1;height:5px;background:#aaa;border-radius:3px;margin-right:60px}

.ribbon{left:632px;width:232px;height:88px}
.ribbon-label{position:absolute;left:60px;top:0;width:172px;height:88px;display:flex;align-items:center;justify-content:center;text-align:center}
.voxly{font-weight:700;font-size:36px;color:var(--red);letter-spacing:-1px}
.donate{font-weight:700;font-size:28px;line-height:27px;color:#8f8f92;letter-spacing:-.5px}
.contacts{font-family:Oswald,sans-serif;font-weight:700;font-size:32px;color:var(--red)}
</style>
</head>
<body>

<div class="abs brand">Quiz Dale Penrose</div>
<div class="abs tagline">life challenges · real solutions</div>

<nav class="abs main-nav">About Dale<span>-</span>Dale’s World<span>-</span>Audio Video<span>-</span>Contact<span>-</span>Donations<span>-</span></nav>

<div class="abs step-art" style="left:134px;top:236px;width:124px;height:148px" role="img" aria-label="Cartoon character looking puzzled"></div>
<div class="abs step-word" style="left:150px;top:390px;width:120px">Ask</div>
<svg class="abs step-arrow" style="left:280px" width="112" height="26" viewBox="0 0 112 26"><path d="M2 13 H106 M92 3 L108 13 L92 23" fill="none" stroke="#d3121b" stroke-width="3"/></svg>

<div class="abs step-art" style="left:420px;top:212px;width:124px;height:140px" role="img" aria-label="Cartoon character smiling"></div>
<div class="abs step-word" style="left:382px;top:370px;width:200px">Receive</div>
<svg class="abs step-arrow" style="left:566px" width="112" height="26" viewBox="0 0 112 26"><path d="M2 13 H106 M92 3 L108 13 L92 23" fill="none" stroke="#d3121b" stroke-width="3"/></svg>

<div class="abs step-art" style="left:704px;top:228px;width:124px;height:140px" role="img" aria-label="Cartoon character laughing"></div>
<div class="abs step-word" style="left:676px;top:390px;width:180px">Achieve</div>

<div class="abs icon-bar">
  <div class="dot"><svg width="14" height="14" viewBox="0 0 14 14"><path d="M7 1 L13 7 H11 V13 H3 V7 H1 Z" fill="#fff"/></svg></div>
  <div class="dot"><svg width="14" height="14" viewBox="0 0 14 14"><path d="M2 2h10v3H2zM2 6h10v3H2zM2 10h10v3H2z" fill="#fff"/></svg></div>
  <div class="dot"><svg width="14" height="14" viewBox="0 0 14 14"><path d="M3 1h6l3 3v9H3z" fill="#fff"/></svg></div>
  <div class="dot"><svg width="14" height="14" viewBox="0 0 14 14"><circle cx="3" cy="11" r="1.6" fill="#fff"/><path d="M2 6a6 6 0 0 1 6 6M2 2a10 10 0 0 1 10 10" fill="none" stroke="#fff" stroke-width="1.8"/></svg></div>
  <div class="dot"><svg width="14" height="14" viewBox="0 0 14 14"><text x="7" y="12" text-anchor="middle" font-family="Arimo,sans-serif" font-weight="700" font-size="13" fill="#fff">?</text></svg></div>
  <div class="dot"><svg width="14" height="14" viewBox="0 0 14 14"><path d="M2 12 L3 9 L10 2 L12 4 L5 11 Z" fill="#fff"/></svg></div>
  <div class="dot"><svg width="14" height="14" viewBox="0 0 14 14"><circle cx="6" cy="6" r="3.5" fill="none" stroke="#fff" stroke-width="2"/><path d="M8.5 8.5 L12.5 12.5" stroke="#fff" stroke-width="2.4"/></svg></div>
  <div class="gap"></div>
  <div class="dot"></div>
  <div class="dot"></div>
  <div class="dot"></div>
  <div class="dot"></div>
  <div class="dot"></div>
  <div class="dot"></div>
</div>

<article class="abs qa-card" style="left:110px">
  <div class="qa-inner">
    <h3 class="qa-title">Love affairs?</h3>
    <p class="qa-cat">Category : Relationships</p>
    <p class="qa-body">Lorem ipsum dolor sit amet, consec<br>etur adipisicing elit, sed do eiusmod<br>&nbsp;tempor &nbsp;incididunt ut labore et dolo<br>re magna aliqua.Ut enim ad minim<br>&nbsp;veniam, quis nostrud exercitation<br>ullamco laboris nisi ut aliquip<br>ex ea commodo consequat.<br>Duis aute irure dolor in reprehenderit<br>in voluptate velit esse cillum dolore<br>&nbsp;fugiat nulla pariatur. Excepteur sint<br>occaecat cupidatat non proident,<br>sunt in culpa qui officia deserunt<br>mollit anim id est laborum</p>
    <div class="more-btn"><svg width="12" height="12" viewBox="0 0 12 12"><circle cx="6" cy="6" r="5" fill="none" stroke="#fff" stroke-width="1.6"/><path d="M6 3v3h2" fill="none" stroke="#fff" stroke-width="1.4"/></svg>MORE</div>
  </div>
</article>

<article class="abs qa-card" style="left:368px">
  <div class="qa-inner">
    <h3 class="qa-title">Not too much...</h3>
    <p class="qa-cat">Category : Healt/Body</p>
    <p class="qa-body">Lorem ipsum dolor sit amet, consec<br>etur adipisicing elit, sed do eiusmod<br>&nbsp;tempor &nbsp;incididunt ut labore et dolo<br>re magna aliqua.Ut enim ad minim<br>&nbsp;veniam, quis nostrud exercitation<br>ullamco laboris nisi ut aliquip<br>ex ea commodo consequat.<br>Duis aute irure dolor in reprehenderit<br>in voluptate velit esse cillum dolore<br>&nbsp;fugiat nulla pariatur. Excepteur sint<br>occaecat cupidatat non proident,<br>sunt in culpa qui officia deserunt<br>mollit anim id est laborum</p>
    <div class="more-btn"><svg width="12" height="12" viewBox="0 0 12 12"><circle cx="6" cy="6" r="5" fill="none" stroke="#fff" stroke-width="1.6"/><path d="M6 3v3h2" fill="none" stroke="#fff" stroke-width="1.4"/></svg>MORE</div>
  </div>
</article>

<article class="abs qa-card" style="left:622px">
  <div class="qa-inner">
    <h3 class="qa-title">Boss in trouble !</h3>
    <p class="qa-cat">Category : Career Work</p>
    <p class="qa-body">Lorem ipsum dolor sit amet, consec<br>etur adipisicing elit, sed do eiusmod<br>&nbsp;tempor &nbsp;incididunt ut labore et dolo<br>re magna aliqua.Ut enim ad minim<br>&nbsp;veniam, quis nostrud exercitation<br>ullamco laboris nisi ut aliquip<br>ex ea commodo consequat.<br>Duis aute irure dolor in reprehenderit<br>in voluptate velit esse cillum dolore<br>&nbsp;fugiat nulla pariatur. Excepteur sint<br>occaecat cupidatat non proident,<br>sunt in culpa qui officia deserunt<br>mollit anim id est laborum</p>
    <div class="more-btn"><svg width="12" height="12" viewBox="0 0 12 12"><circle cx="6" cy="6" r="5" fill="none" stroke="#fff" stroke-width="1.6"/><path d="M6 3v3h2" fill="none" stroke="#fff" stroke-width="1.4"/></svg>MORE</div>
  </div>
</article>

<section class="abs video-panel"><div class="video-inner"></div></section>
<h2 class="abs video-heading">Video</h2>
<div class="abs video-frame" role="img" aria-label="Video still of two men talking in a kitchen">
  <div class="video-title">Dad Talks Back - Fall 2010 Preview</div>
  <div class="video-play"><svg width="18" height="20" viewBox="0 0 18 20"><path d="M2 1 L17 10 L2 19 Z" fill="#333"/></svg></div>
  <div class="video-mark">Vidlane</div>
  <div class="video-controls"><svg width="10" height="10" viewBox="0 0 10 10"><path d="M1 0 L10 5 L1 10 Z" fill="#222"/></svg><span>0:00 / 2:52</span><div class="track"></div></div>
</div>

<svg class="abs ribbon" style="top:886px" viewBox="0 0 232 88" width="232" height="88"><polygon points="0,0 232,0 232,88 0,88 36,44" fill="var(--ribbon)"/></svg>
<div class="abs ribbon" style="top:886px"><div class="ribbon-label"><span class="voxly">VOXLY</span></div></div>

<svg class="abs ribbon" style="top:994px" viewBox="0 0 232 88" width="232" height="88"><polygon points="0,0 232,0 232,88 0,88 36,44" fill="var(--ribbon)"/></svg>
<div class="abs ribbon" style="top:994px"><div class="ribbon-label"><span class="donate">Make a<br>Donation</span></div></div>

<svg class="abs ribbon" style="top:1100px" viewBox="0 0 232 88" width="232" height="88"><polygon points="0,0 232,0 232,88 0,88 36,44" fill="var(--ribbon)"/></svg>
<div class="abs ribbon" style="top:1100px"><div class="ribbon-label"><span class="contacts">Contacts</span></div></div>

</body>
</html>
```